Web Pages Improvement, Update of existing BRUN website

Redesign existing website www.brun.asn.au The # of pages can be reduced to a total of 6 including the home page. We have a design project out for the logo for this site so feel free to bid for that also.
As this is a simple brief with basic pages, we expect the end result to be code ready for uploaded to our existing host.

```html
<!DOCTYPE html>
<html lang="en">
<head>
<meta charset="utf-8">
<title>BRUN – Broadline Regulatory Unit Network</title>
<link rel="stylesheet" href="https://fonts.googleapis.com/css2?family=Ubuntu:wght@400;500&family=Crimson+Text&display=swap">
<style>
  :root {
    --orange: #f26a0c;
    --orange-bright: #ff8a1a;
    --text: #2b2b2b;
    --nav-top: #5a5a5a;
    --nav-bottom: #1e1e1e;
    --header-dark: #2f3a38;
    --header-mid: #6f8583;
    --header-light: #a9bcba;
    --footer-top: #2a5ca0;
    --footer-bottom: #0d2e63;
    --sidebar: #f2f2f2;
    --member-text: #3a3a6a;
    --white: #ffffff;
  }
  * { margin: 0; padding: 0; box-sizing: border-box; }
  html, body { width: 1200px; height: 1000px; overflow: hidden; }
  body { position: relative; background: var(--white); font-family: Arial, Helvetica, sans-serif; color: var(--text); }

  .site-header {
    position: absolute; left: 0; top: 0; width: 1200px; height: 510px;
    background:
      radial-gradient(ellipse at 70% 10%, rgba(220,235,232,.55), transparent 55%),
      linear-gradient(160deg, var(--header-light) 0%, var(--header-mid) 35%, var(--header-dark) 100%);
  }
  .brand { position: absolute; left: 98px; top: 28px; }
  .brand-row { display: flex; align-items: center; gap: 12px; }
  .brand-square { width: 30px; height: 30px; background: var(--orange); }
  .brand-name { font-family: "Ubuntu", sans-serif; font-weight: 500; font-size: 38px; line-height: 40px; color: var(--white); }
  .brand-tagline { margin-top: 8px; font-size: 11px; line-height: 13px; color: var(--white); }

  .contact-strip { position: absolute; right: 86px; top: 28px; font-family: "Crimson Text", serif; color: var(--white); }
  .contact-row { display: flex; align-items: center; gap: 12px; height: 28px; justify-content: flex-end; }
  .contact-row.phone { font-size: 22px; }
  .contact-row.mail { font-size: 16px; }

  .main-nav { position: absolute; left: 78px; top: 104px; width: 1050px; height: 42px; display: flex;
    background: linear-gradient(var(--nav-top), var(--nav-bottom)); }
  .main-nav a { display: flex; align-items: center; justify-content: center; height: 42px; color: var(--white);
    text-decoration: none; font-family: "Ubuntu", sans-serif; font-size: 15px; text-transform: uppercase; border-right: 1px solid #111; }
  .main-nav a.active { background: linear-gradient(var(--orange-bright), var(--orange)); }

  .hero-frame { position: absolute; left: 78px; top: 146px; width: 1050px; height: 360px; background: var(--white); padding: 8px 6px 8px 7px; }
  .hero-image { width: 100%; height: 100%;
    background: linear-gradient(180deg, #9aa6a4 0%, #4b5a4c 35%, #2e6a3a 55%, #d9dbd8 72%, #4f8fc9 88%, #3a6fa8 100%); }

  .welcome { position: absolute; left: 79px; top: 530px; width: 766px; }
  .welcome h1 { font-family: "Ubuntu", sans-serif; font-weight: 400; font-size: 22px; color: var(--orange); margin-bottom: 13px; }
  .welcome p { font-size: 12px; line-height: 17px; text-align: justify; margin-bottom: 17px; }

  .sidebar { position: absolute; left: 870px; top: 510px; width: 330px; height: 434px;
    background: linear-gradient(90deg, #e9e9e9 0, var(--sidebar) 14px, var(--sidebar) 100%); }
  .sidebar h2 { position: absolute; left: 16px; font-family: "Ubuntu", sans-serif; font-weight: 400; font-size: 15px; color: var(--orange); white-space: nowrap; }
  .member-grid { position: absolute; left: 22px; top: 70px; display: grid; grid-template-columns: 120px 120px; grid-auto-rows: 73px; }
  .member-name { font-family: "Ubuntu", sans-serif; font-weight: 500; font-size: 14px; color: var(--member-text);
    display: flex; align-items: center; gap: 6px; height: 44px; white-space: nowrap; }
  .member-name .dot { width: 12px; height: 12px; border-radius: 50%; background: var(--orange); flex: none; }
  .badge-row { position: absolute; left: 22px; top: 350px; display: flex; gap: 24px; }
  .badge { width: 26px; height: 26px; border-radius: 50%; background: #111; }
  .badge.square { border-radius: 3px; }

  .site-footer { position: absolute; left: 0; top: 944px; width: 1200px; height: 56px;
    background: linear-gradient(var(--footer-top), var(--footer-bottom)); }
  .footer-nav { position: absolute; left: 79px; top: 20px; font-family: "Ubuntu", sans-serif; font-size: 11px; color: var(--white); }
  .footer-nav a { color: var(--white); text-decoration: none; }
  .footer-nav span { margin: 0 4px; }
</style>
</head>
<body>
  <header class="site-header">
    <div class="brand">
      <div class="brand-row">
        <span class="brand-square"></span>
        <span class="brand-name">BRUN</span>
      </div>
      <div class="brand-tagline">Broadline Regulatory Unit Network</div>
    </div>
    <div class="contact-strip">
      <div class="contact-row phone">
        <svg width="18" height="12" viewBox="0 0 18 12"><rect x=".5" y=".5" width="17" height="11" fill="#222" stroke="#fff"/><path d="M1 1l8 6 8-6" fill="none" stroke="#fff"/></svg>
        +61 (0)3 9000 4127
      </div>
      <div class="contact-row mail">
        <svg width="16" height="12" viewBox="0 0 16 12"><path d="M1 4c3-3 11-3 14 0l-2 2-2-1V3H5v2L3 6z" fill="#fff"/><rect x="3" y="6" width="10" height="6" rx="1" fill="#fff"/></svg>
        office@brun.com.au
      </div>
    </div>
    <nav class="main-nav">
      <a class="active" href="#" style="width:130px">Overview</a>
      <a href="#" style="width:250px">Statement of Purpose</a>
      <a href="#" style="width:191px">Types of Testing</a>
      <a href="#" style="width:185px">Member Listing</a>
      <a href="#" style="width:112px">Member</a>
      <a href="#" style="width:114px">Contact</a>
      <a href="#" style="width:68px;border-right:0">Link</a>
    </nav>
    <div class="hero-frame">
      <div class="hero-image" role="img" aria-label="Photo of an electrical control panel with rows of terminal modules and blue wiring"></div>
    </div>
  </header>

  <main class="welcome">
    <h1>WELCOME TO BRUN</h1>
    <p>The Broadline Regulatory Unit Network of Australia (BRUN) was established in 1995 to foster the growth of a professional and value adding compliance testing resource to serve the needs of Australian industry.</p>
    <p>BRUN is an incorporated association formed by QALA accredited electrical testing laboratories in Australia and includes an accredited member from New Zealand. The association has 14 active members which operate laboratories in a total of 18 locations in Australia and New Zealand. The members provide testing services to the public in the areas of electrical safety, electromagnetic compatibility, electromagnetic radiation, electromedical equipment, energy efficiency labelling, environmental performance, gas appliances, lighting equipment, performance ratings, and telecommunications. The QALA accreditation mark is shown below.</p>
    <p>The Association operates a paid secretariat to service the interests of its members and to provide information about the services available to the public from its members. The registered office is in Northbank, Victoria. The members of BRUN meet regularly to discuss issues of interest to its members and the testing industry and to make submissions to regulators, public investigations, inquiries and industry surveys. The Association nominates members to serve on relevant Committees of the National Standards Board and to make representations to government inquiries.</p>
    <p>Member laboratories of BRUN test equipment to Australian and International Standards so that the clients are able to apply the appropriate regulatory mark for their product. The commonly recognised regulatory marks are the K-Mark and V-Mark for Australia, E-Mark for Europe, U-Mark for the USA as shown below.</p>
  </main>

  <aside class="sidebar">
    <h2 style="top:22px">BRUN MEMBER</h2>
    <div class="member-grid">
      <div class="member-name"><span class="dot"></span>Meridian Labs</div>
      <div class="member-name"><span class="dot"></span>voltara</div>
      <div class="member-name"><span class="dot"></span>kelvane</div>
      <div class="member-name"><span class="dot"></span>Testwise</div>
      <div class="member-name"><span class="dot"></span>Lumora</div>
      <div class="member-name"><span class="dot"></span>Harrow Labs</div>
    </div>
    <h2 style="top:313px">MEMBER LABORATORIES OF BRUN</h2>
    <div class="badge-row">
      <div class="badge square"></div>
      <div class="badge"></div>
      <div class="badge square"></div>
      <div class="badge"></div>
      <div class="badge square"></div>
    </div>
  </aside>

  <footer class="site-footer">
    <nav class="footer-nav">
      <a href="#">Home</a><span>|</span><a href="#">Overview</a><span>|</span><a href="#">Statement of Purpose</a><span>|</span><a href="#">Types of Testing</a><span>|</span><a href="#">Members Details</a><span>|</span><a href="#">Member Geographical</a><span>|</span><a href="#">Contact</a><span>|</span><a href="#">Links</a><span>|</span><a href="#">Site Map</a>
    </nav>
  </footer>
</body>
</html>
```